Business Card Design Project

Business Card
We are rebranding with a new logo
Industry/Entity Type
Business
Contact Information for Business Card
Dennis Marlow +61 427581962 dennis@qovo.com.au P.O. Box 872 Kelvindale QLD 4309
Requirements
Must have
- Logo

```html
<!DOCTYPE html>
<html lang="en">
<head>
<meta charset="utf-8">
<title>Qovo International – Business Card</title>
<link rel="stylesheet" href="https://fonts.googleapis.com/css2?family=Mulish:wght@400;600;700&display=swap">
<style>
  :root {
    --page-bg: #eceef1;
    --card-white: #f7f7f8;
    --card-blue: #6f97cf;
    --card-blue-light: #7fa4d6;
    --ink-blue: #5f84c4;
    --rule-blue: #6f8fc8;
    --white: #ffffff;
  }
  * { margin: 0; padding: 0; box-sizing: border-box; }
  html, body {
    width: 1200px; height: 800px; overflow: hidden;
    background: var(--page-bg);
    font-family: "Mulish", Verdana, sans-serif;
  }
  .canvas {
    position: relative; width: 1200px; height: 800px;
    display: flex; align-items: center; justify-content: center; gap: 40px;
  }
  .card {
    position: relative; width: 540px; height: 300px; overflow: hidden;
    box-shadow: 0 10px 30px rgba(40, 50, 70, 0.18);
  }

  /* Back side */
  .card--back {
    background: linear-gradient(135deg, var(--card-blue) 0%, var(--card-blue-light) 100%);
  }
  .back-brand {
    position: absolute; left: 50%; top: 50%; transform: translate(-50%, -50%);
    text-align: center; color: var(--white); font-weight: 700;
  }
  .back-brand .brand-name { font-size: 58px; line-height: 1; letter-spacing: 1px; }
  .back-brand .brand-sub { font-size: 14px; letter-spacing: 4px; margin-top: 6px; }

  /* Front side */
  .card--front {
    background: var(--card-white);
    display: flex; align-items: center; padding: 0 30px 0 40px;
  }
  .front-brand {
    width: 210px; text-align: center; color: var(--ink-blue); font-weight: 700;
  }
  .front-brand .brand-name { font-size: 56px; line-height: 1; letter-spacing: 1px; }
  .front-brand .brand-sub { font-size: 13px; letter-spacing: 3.5px; margin-top: 8px; }
  .divider {
    width: 2px; height: 140px; background: var(--rule-blue); margin: 0 28px 0 22px;
  }
  .contact { color: var(--ink-blue); font-size: 15px; letter-spacing: 1px; white-space: nowrap; }
  .contact-name {
    font-size: 18px; font-weight: 700; letter-spacing: 1.5px;
    padding-bottom: 3px; border-bottom: 2px solid var(--rule-blue);
    margin-bottom: 10px; display: inline-block;
  }
  .contact-line { display: flex; align-items: center; gap: 6px; line-height: 22px; }
  .contact-line svg { width: 12px; height: 12px; fill: var(--ink-blue); flex: none; }
  .contact-line--indent { padding-left: 18px; }
</style>
</head>
<body>
<main class="canvas">
  <section class="card card--back" aria-label="Card back">
    <div class="back-brand">
      <div class="brand-name">Qovo</div>
      <div class="brand-sub">INTERNATIONAL</div>
    </div>
  </section>

  <section class="card card--front" aria-label="Card front">
    <div class="front-brand">
      <div class="brand-name">Qovo</div>
      <div class="brand-sub">INTERNATIONAL</div>
    </div>
    <div class="divider"></div>
    <div class="contact">
      <div class="contact-name">DENNIS MARLOW</div>
      <div class="contact-line">
        <svg viewBox="0 0 24 24" aria-hidden="true"><path d="M6.6 10.8a15.2 15.2 0 0 0 6.6 6.6l2.2-2.2a1 1 0 0 1 1-.25 11.4 11.4 0 0 0 3.6.57 1 1 0 0 1 1 1V20a1 1 0 0 1-1 1A17 17 0 0 1 3 4a1 1 0 0 1 1-1h3.5a1 1 0 0 1 1 1c0 1.25.2 2.45.57 3.57a1 1 0 0 1-.25 1z"/></svg>
        <span>+61 427581962</span>
      </div>
      <div class="contact-line">
        <svg viewBox="0 0 24 24" aria-hidden="true"><path d="M2 5h20v14H2z"/><path d="M3 6l9 7 9-7" fill="none" stroke="#f7f7f8" stroke-width="2"/></svg>
        <span>dennis@qovo.com.au</span>
      </div>
      <div class="contact-line">
        <svg viewBox="0 0 24 24" aria-hidden="true"><path d="M12 2a7 7 0 0 0-7 7c0 5 7 13 7 13s7-8 7-13a7 7 0 0 0-7-7zm0 9.5A2.5 2.5 0 1 1 12 6.5a2.5 2.5 0 0 1 0 5z"/></svg>
        <span>Kelvindale QLD 4309</span>
      </div>
      <div class="contact-line contact-line--indent"><span>P.O. Box 872</span></div>
    </div>
  </section>
</main>
</body>
</html>
```